Business card for a boutique travel agency VELARIEN

we need a business card design - double sided. We would like to have a very elegant, sophisticated but modern design. we are travel consultants and our business focus is Europe, mainly the city of Paris. We would like to receive designs in white and silver, black color but if you are confident that we should pick up a color to make it different and more beautful...go ahead! We are going to give business cards to our clients and business partners. It is important to be perceived as elegant, modern and trustful. Please check jpg references.

Target Market(s)

Velarien primary clients are individuals, couples and affinity groups of high-net-worth who travel for leisure at least once per year. Seeking the ultimate travel experience, the target clients demand the finest quality activities and accommodations accompanied by a superior level of service.

Industry/Entity Type

Travel Industry

Contact Information for Business Card

Lucinda Farrow
- lucinda@velarien-example.com
- +55 11 98347.2516
- velarien-example.com
- unique travel experiences (we would like to see this signature printed as a detail)

Font styles to use
Sans Serif

Colors

Designer to choose colors to be used in the design.

Requirements
Must have
• the Velarien logo that I have attached
Nice to have
• we would like to have some nice detail, something different that shows that we care about,... we are detail oriented.
Should not have
• decorative fonts

```html
<!DOCTYPE html>
<html lang="en">
<head>
<meta charset="utf-8">
<title>Velarien — Business Card</title>
<link rel="stylesheet" href="https://fonts.googleapis.com/css2?family=Montserrat:wght@300;400&family=Open+Sans:wght@400&display=swap">
<style>
  :root {
    --stage: #8c8c8c;
    --card-white: #ffffff;
    --card-black: #050505;
    --ink-dark: #111111;
    --ink-light: #ffffff;
    --ink-soft: #e6e6e6;
  }
  * { margin: 0; padding: 0; box-sizing: border-box; }
  html, body {
    width: 1200px; height: 1200px; overflow: hidden;
    background: var(--stage);
  }
  .stage {
    width: 1200px; height: 1200px;
    display: flex; flex-direction: column;
    align-items: center; justify-content: center;
    gap: 70px;
  }
  .card {
    position: relative;
    width: 860px; height: 491px;
    border-radius: 44px;
    overflow: hidden;
    box-shadow: 0 18px 40px rgba(0,0,0,0.28);
  }

  /* Front */
  .card--front {
    background: var(--card-white);
    display: flex; align-items: center; justify-content: center;
  }
  .wordmark {
    font-family: "Montserrat", sans-serif;
    font-weight: 300;
    letter-spacing: 0.42em;
    text-transform: uppercase;
  }
  .card--front .wordmark {
    color: var(--ink-dark);
    font-size: 40px;
    margin-right: -0.42em;
  }

  /* Back */
  .card--back {
    background: var(--card-black);
    color: var(--ink-light);
  }
  .back-circle {
    position: absolute;
    top: -70px; right: -40px;
    width: 320px; height: 320px;
  }
  .holder {
    position: absolute;
    left: 54px; top: 176px;
  }
  .holder__name {
    font-family: "Open Sans", sans-serif;
    font-weight: 400;
    font-size: 34px;
    letter-spacing: 0.02em;
    text-transform: uppercase;
    margin-bottom: 12px;
  }
  .contact {
    font-family: "Open Sans", sans-serif;
    font-size: 17px;
    line-height: 27px;
    color: var(--ink-soft);
    border-collapse: collapse;
  }
  .contact th {
    font-weight: 400;
    text-align: left;
    width: 78px;
  }
  .contact td::before { content: ": "; }
  .signature {
    position: absolute;
    left: 54px; top: 350px;
    width: 600px;
  }
  .signature__tagline {
    font-family: "Open Sans", sans-serif;
    font-size: 16px;
    letter-spacing: 0.04em;
    text-transform: uppercase;
    color: var(--ink-soft);
    padding-bottom: 8px;
    border-bottom: 2px dotted var(--ink-soft);
  }
  .card--back .wordmark {
    display: block;
    margin-top: 12px;
    font-size: 46px;
    color: var(--ink-light);
  }
</style>
</head>
<body>
  <main class="stage">
    <section class="card card--front" aria-label="Business card front">
      <span class="wordmark">Velarien</span>
    </section>

    <section class="card card--back" aria-label="Business card back">
      <svg class="back-circle" viewBox="0 0 320 320" aria-hidden="true">
        <circle cx="160" cy="160" r="150" fill="var(--card-white)"/>
      </svg>

      <div class="holder">
        <h1 class="holder__name">Lucinda Farrow</h1>
        <table class="contact">
          <tr><th>Tel</th><td>+55 11 98347.2516</td></tr>
          <tr><th>Web</th><td>velarien-example.com</td></tr>
          <tr><th>Email</th><td>lucinda@velarien-example.com</td></tr>
        </table>
      </div>

      <div class="signature">
        <p class="signature__tagline">Unique travel experiences</p>
        <span class="wordmark">Velarien</span>
      </div>
    </section>
  </main>
</body>
</html>
```